New webdesign for a cable company

We need a new design for Lunor Media.

There exist a suggestion for the page, were we have attached files to show you this. The design here is not good enough, but here you can se what content we need.

You can feel free to give adjustment to this design to make it better, our blow us away with a new brilliant design, but from this design you see what content we need.

The important is that the company get a design who represent its products:
- TV = Cable TV
- Bredbånd = Broadband
- Mobil = Mobile phone
- Strøm = Electricity
- Alarm = Alarm
- Lunor Komplett = a cobain pagage of all our products.

Lunor Media would like costumers who visit the site to het the impression that Lunor Media is a professional, innovative and fun company.
Updates

We have to day uploaded pictures of the existing page as the link haven't been working for the most of you as it's placed on a server our developer are using and is often shut it down. 

We have also updated the brief with some new and updated description so please read true the updated brief. 

We will at the same time inform that we haven't been able to give feedback on any of the received design and are sorry for that, we will within the next 24 hours hopefully have started responded the different received designs.

Looking forward to see more suggestion and hope you will help us create and very professional and informative design. 

Reason: We have decided to extend the deadline due to the number of design suggestion who is sent in and your lack of response to all designers due to our own workload.

This project was unfortunately for different reason put on ice for a while, but we are now ready to complete the design and will answer and give feedback too all the received design suggestions. 

Within a couple of days we hope we have answered all you who sent us suggestions, we appreciate all suggestions and hope to get in more suggestions.

Reason: Deisgn description have been updated

Target Market(s)

Our costumer are both private and companies

Industry/Entity Type

Tv

Requirements
Must have
• A easy way to promote and inform about changes in our products, there are a constant change in our products and it must bee a easy and good way to changes ass the marked change. Cheek out this link, for a example of what we like/think of here, https://kabel.fjordvisjon.no

On all pages there must be a easy way to click on a order button and too inform about your interest (thats two different things), could be placed in the top right corner for example. In the order form you should follow a step by step part:
1. Cheek what product we can provide you.
2. Chooce products.
3. Costumer inforamtion.
4. Confirmation.

Somewere on the portal it must be possible for costumers to log on to their own administration, where they can cheek for invoices, other statuses, etc.

A main menu existing of:
Hjem (Home)
Produkter (Products)
Storkunde (key account/large costumers)
Kundeservice (Costumerservice)
Min side (My page)

The main menu should have the following sub titles:
- Under "Produkter"/products our different products must be listed
- Under "Kundeservice"/Costumerservice it must have these submenus:
- Hjelp og støtte = Help.
- Faktura = Invoice
- Brukerguider = Userguides
- Abbonementavtaler = Terms and conditions.

A bottom menu where we have 5 main categories, with sub categories:
Om oss (about us)
- Om Lunor Media (about Lunor Media)
- Kontaktinformajson ( contact information)
- Pressemeldinger (Pressrelese)
- Ledige stillinger (positions available)
- KRAN ( and organisastion in our field)

Produkter (Product)
- TV (TV)
- Bredbånd (Broadand)
- Telefoni (telephony, both mobil)
- Strøm (elecricity)
- Arlam (Alarm)

Borrettslag/Sameier (Housing cooperatives)
- Løsninger (solutions)
- Produkter (product)
- Kontaktpersoner (contactpersons)

Utbygger (developer)
- Hva vi kan gjøre for dere. (What we can do for you)

Opperatørnett (operators)

Build up the categories and bottom menu something like this:
https://kabel.fjordvisjon.no
www.tavrik.com
Nice to have
• A main menu existing of:
Hjem (Home)
Produkter (Products)
Lunor Media
Kontakt oss (Contact us)

Under "Produkter"/products our different products must be listed and under "Kundeservice"/Costumerservice it must have these submenus:
- Hjelp og støtte = Help.
- Faktura = Invoice
Should not have
• Any translation section since the homepage only will be in Norwegian.

```html
<!DOCTYPE html>
<html lang="no">
<head>
<meta charset="utf-8">
<title>Lunor Media – Kundeservice</title>
<link href="https://fonts.googleapis.com/css2?family=PT+Sans:wght@400;700&family=Ubuntu:wght@400;700&display=swap" rel="stylesheet">
<style>
:root{
  --orange:#f7860f;
  --orange-btn:#f4650a;
  --blue:#1a63d4;
  --blue-dark:#0b4fc0;
  --ink:#333;
  --muted:#555;
  --panel:#e8edf2;
  --panel-border:#cdd3d9;
  --footer:#474747;
  --footer-box:#5f5f5f;
  --footer-line:#5a5a5a;
  --footer-text:#eaeaea;
}
*{box-sizing:border-box;margin:0;padding:0}
html,body{width:1029px;height:1200px;overflow:hidden}
body{position:relative;background:#fff;font-family:"PT Sans",sans-serif;color:var(--ink)}
.abs{position:absolute}

.site-header{position:absolute;left:0;top:0;width:1029px;height:90px;background:#fff;
  background-image:repeating-linear-gradient(90deg,#e4e4e4 0 1px,transparent 1px 3px);background-size:100% 14px;background-repeat:no-repeat}
.brand{position:absolute;left:136px;top:26px;display:flex;align-items:center;gap:8px;font-size:27px;color:#2a4f8e;font-family:"PT Sans",sans-serif}
.brand-mark{width:22px;height:22px;border-radius:50%;background:#2a4f8e}
.main-nav{position:absolute;left:367px;top:38px;display:flex;gap:16px;font-size:14px}
.main-nav a{color:#333;text-decoration:none}
.main-nav a.active{color:var(--orange)}
.call-hours{position:absolute;right:130px;top:15px;font-size:10.5px;color:#666}
.call-number{position:absolute;right:130px;top:35px;font-size:20px;color:#555;display:flex;align-items:center;gap:6px}

.hero{position:absolute;left:0;top:90px;width:1029px;height:300px;background:linear-gradient(180deg,var(--blue-dark),var(--blue) 60%,#2a78e0)}
.hero-strip{position:absolute;left:133px;top:10px;width:775px;height:78px;
  background-image:repeating-linear-gradient(90deg,rgba(255,255,255,.06) 0 28px,transparent 28px 44px);opacity:.8}
.hero h1{position:absolute;left:144px;top:22px;font-family:"PT Sans",sans-serif;font-weight:400;font-size:41px;color:#fff;text-shadow:0 2px 3px rgba(0,0,0,.35)}

.content-card{position:absolute;left:133px;top:178px;width:775px;height:757px;background:#fff;box-shadow:0 0 4px rgba(0,0,0,.2)}
.page-title{position:absolute;left:172px;top:212px;font-family:"Ubuntu",sans-serif;font-weight:700;font-size:33px;color:var(--orange);text-shadow:0 2px 2px rgba(0,0,0,.2)}

.panel{position:absolute;background:var(--panel);border:1px solid var(--panel-border);border-radius:5px;box-shadow:1px 2px 3px rgba(0,0,0,.18)}
.article{left:173px;top:282px;width:432px;height:621px}
.photo{position:absolute;left:19px;top:20px;width:124px;height:95px;border:2px solid #9aa;background:linear-gradient(135deg,#5e6f84,#8a8fa8 55%,#3f4a55)}
.article-text{position:absolute;left:22px;top:20px;width:390px;font-family:Arial,sans-serif;font-size:10.3px;line-height:14.5px;color:#444}
.article-text p{margin-bottom:14.5px}
.float-gap{float:left;width:131px;height:98px}
.btn-form{position:absolute;left:224px;top:567px;width:100px;height:22px;border:1px solid #b9bcc0;background:#f2f4f6;font-size:13px;color:#777;display:flex;align-items:center;justify-content:center;gap:6px}

.sidebar{left:622px;top:282px;width:247px;height:621px;padding:0 9px}
.side-group{border-bottom:1px solid #d6dce2;padding:13px 0 10px 7px}
.side-group h3{font-weight:400;font-size:17.5px;color:#333;margin-bottom:9px}
.side-group li{list-style:none;font-size:11px;color:#222;line-height:19.5px;display:flex;align-items:center;gap:8px}
.side-group li::before{content:"›";font-weight:700;font-size:15px;line-height:1}

.site-footer{position:absolute;left:0;top:935px;width:1029px;height:265px;background:var(--footer);color:var(--footer-text)}
.ft-title{position:absolute;font-size:17.5px;color:#fff}
.ft-rule{position:absolute;height:1px;background:var(--footer-line)}
.contact-row{position:absolute;left:146px;display:flex;gap:8px;font-size:11px;line-height:14.5px;width:210px}
.contact-row svg{flex:none}
.feed{position:absolute;left:386px;top:54px;width:270px;height:154px;background:var(--footer-box)}
.feed::before{content:"";position:absolute;left:42px;top:-14px;border-left:20px solid transparent;border-bottom:14px solid var(--footer-box)}
.feed-item{margin:0 15px;padding:13px 10px 6px;border-bottom:1px solid #777;font-family:Arial,sans-serif;font-size:8.3px;line-height:10px;color:#ddd}
.feed-item:last-child{border:0}
.feed-item .date{text-align:right;margin-top:4px;font-size:8.5px}
.sub-label{position:absolute;left:709px;font-family:Arial,sans-serif;font-size:9.5px;color:#eee}
.sub-input{position:absolute;left:748px;width:150px;height:22px;background:#6a6a6a}
.sub-btn{position:absolute;left:748px;top:134px;width:86px;height:23px;background:var(--orange-btn);color:#fff;font-size:13px;display:flex;align-items:center;justify-content:center}
.copyright{position:absolute;left:170px;top:244px;font-family:Arial,sans-serif;font-size:9.5px;color:#bbb}
</style>
</head>
<body>

<header class="site-header">
  <div class="brand"><span class="brand-mark"></span>Lunor Media</div>
  <nav class="main-nav">
    <a href="#">Hjem</a><a href="#">Produkter</a><a href="#" class="active">Kundeservice</a><a href="#">Om oss</a><a href="#">Kontakt oss</a>
  </nav>
  <div class="call-hours">Ring oss hverdager 10:00 - 15:00</div>
  <div class="call-number">
    <svg width="10" height="18" viewBox="0 0 10 18"><path d="M3 1 L6 1 L7 5 L5 6 Q4 9 5 12 L7 13 L6 17 L3 17 Q0 9 3 1Z" fill="#f7860f"/></svg>
    41 27 38 90
  </div>
</header>

<section class="hero">
  <div class="hero-strip"></div>
  <h1>Kundeservice</h1>
</section>

<main class="content-card"></main>
<h2 class="page-title">Dignissim pretium veroeros</h2>

<article class="panel article">
  <div class="photo" role="img" aria-label="Foto av en jente i sofaen med fjernkontroll"></div>
  <div class="article-text">
    <div class="float-gap"></div>
    <p>Lorem ipsum dolor sit amet, consectetur adipisicing elitLorem ipsum dolor.Lorem ipsum dolor sit amet, consectetur adipisicing elitLorem ipsum dolor. Lorem ipsum dolor sit amet, consectetur adipisicing elitLorem ipsum dolor.elitLorem ipsum dolor. Lorem ipsum dolor sit amet, consectetur adipisicing elitLorem ipsum dolor. Lorem ipsum dolor sit amet, consectetur adipisicing elitLorem ipsum dolor.Lorem ipsum dolor sit amet, consectetur adipisicing elitLorem ipsum dolor. Lorem ipsum dolor sit amet, consectetuadipisicingelitLoremipsumdolor.elitLorem ipsum doloLorem ipsum dolor sit amet, consectetur adipisicing elitLorem ipsum dolor.</p>
    <p>Lorem ipsum dolor sit amet, consectetur adipisicing elitLorem ipsum dolor.Lorem ipsum dolor sit amet, consectetur adipisicing elitLorem ipsum dolor. Lorem ipsum dolor sit amet, consectetuadipisicingelitLoremipsumdolor.elitLorem ipsum doloLorem ipsum dolor sit amet, consectetur adipisicing elitLorem ipsum dolor.Lorem ipsum dolor sit amet, consectetur adipisicing elitLorem ipsum dolor.Lorem ipsum dolor sit amet, consectetur adipisicing elitLorem ipsum dolor. Lorem ipsum dolor sit amet, consectetuadipisicingelitLoremipsumdolor.elitLorem ipsum doloLorem ipsum dolor sit amet, consectetur adipisicing elitLorem ipsum dolor.</p>
    <p>Lorem ipsum dolor sit amet, consectetur adipisicing elitLorem ipsum dolor.Lorem ipsum dolor sit amet, consectetur adipisicing elitLorem ipsum dolor. Lorem ipsum dolor sit amet, consectetuadipisicingelitLoremipsumdolor.elitLorem ipsum doloLorem ipsum dolor sit amet, consectetur adipisicing elitLorem ipsum dolor.</p>
  </div>
  <a class="btn-form">Sind skjema <span style="font-weight:700;font-size:16px">›</span></a>
</article>

<aside class="panel sidebar">
  <div class="side-group"><h3>Help og stotte</h3><ul><li>Bredband tilgjengelig.</li><li>Trykk her for pris of ingo...</li><li>Bredband ikke tilgjengelig.</li><li>Trykk her for pris og info...</li><li>Bredband ikke tilgjengelig.</li></ul></div>
  <div class="side-group" style="padding-top:16px"><h3>Faktura</h3><ul><li>Bredband tilgjengelig.</li><li>Trykk her for pris of ingo...</li><li>Bredband ikke tilgjengelig.</li><li>Trykk her for pris og info...</li></ul></div>
  <div class="side-group" style="padding-top:20px"><h3>Brukerguider</h3><ul><li>Bredband tilgjengelig.</li><li>Trykk her for pris of ingo...</li><li>Bredband ikke tilgjengelig.</li><li>Trykk her for pris og info...</li></ul></div>
  <div class="side-group" style="padding-top:19px"><h3>Abonnement/avtaler</h3><ul><li>Bredband tilgjengelig.</li><li>Trykk her for pris of ingo...</li><li>Bredband ikke tilgjengelig.</li><li>Trykk her for pris og info...</li></ul></div>
</aside>

<footer class="site-footer">
  <div class="ft-title" style="left:146px;top:21px">Kontakt oss</div>
  <div class="ft-rule" style="left:146px;top:52px;width:200px"></div>
  <div class="contact-row" style="top:66px">
    <svg width="12" height="16" viewBox="0 0 12 16"><path d="M6 0a6 6 0 0 0-6 6c0 4 6 10 6 10s6-6 6-10a6 6 0 0 0-6-6zm0 8.5a2.5 2.5 0 1 1 0-5 2.5 2.5 0 0 1 0 5z" fill="#fff"/></svg>
    <span>Lorem ipsum dolor sit amet, consectetur adipisicing elit, sed do eiusmod tempor eiusmod tempor</span>
  </div>
  <div class="contact-row" style="top:118px">
    <svg width="12" height="16" viewBox="0 0 10 18"><path d="M3 1 L6 1 L7 5 L5 6 Q4 9 5 12 L7 13 L6 17 L3 17 Q0 9 3 1Z" fill="#fff"/></svg>
    <span>41 27 38 90</span>
  </div>
  <div class="contact-row" style="top:147px">
    <svg width="16" height="12" viewBox="0 0 16 12"><rect width="16" height="12" fill="#fff"/><path d="M0 0l8 7 8-7" stroke="#474747" stroke-width="1.5" fill="none"/></svg>
    <span>post@lunormedia.no</span>
  </div>

  <div class="ft-title" style="left:489px;top:23px;font-size:15px">Kvitter Stream</div>
  <div class="feed">
    <div class="feed-item">Lorem ipsum dolor sit amet, consectetur adipisicing elit, sed do eiusmod tempor<div class="date">07,May 2013</div></div>
    <div class="feed-item">Lorem ipsum dolor sit amet, consectetur adipisicing elit, sed do eiusmod tempor<div class="date">07,May 2013</div></div>
    <div class="feed-item">Lorem ipsum dolor sit amet, consectetur adipisicing elit, sed do eiusmod tempor<div class="date">07,May 2013</div></div>
  </div>

  <div class="ft-title" style="left:710px;top:21px">Subscribe</div>
  <div class="ft-rule" style="left:710px;top:52px;width:198px"></div>
  <div class="sub-label" style="top:69px">Name:</div><div class="sub-input" style="top:62px"></div>
  <div class="sub-label" style="top:104px">Email:</div><div class="sub-input" style="top:97px"></div>
  <div class="sub-btn">Subscribe &nbsp;&gt;</div>

  <div class="ft-rule" style="left:133px;top:230px;width:775px"></div>
  <div class="copyright">@ Copyright 2013 &nbsp;| &nbsp;LunorMedia &nbsp; All rights reserved.</div>
</footer>

</body>
</html>
```